a Sydney based app company needs a product booklet

we need a 8 pager booklet to introduce the key benefit of our app. The content is included in the doc attached. Also can refer to the design style in our website quillora.au. A updated content doc has been uploaded. Please also add to the end cover 'Powered by OFR' with OFR logo which is also attached.

Retail customers

```html
<!DOCTYPE html>
<html lang="en">
<head>
<meta charset="utf-8">
<title>Quillora Booklet – Pages 4 to 7</title>
<link href="https://fonts.googleapis.com/css2?family=Raleway:wght@500;600;700;800&family=Poppins:wght@500;600;700&display=swap" rel="stylesheet">
<style>
  :root{
    --blue:#0a4f9c;
    --orange:#e69a00;
    --ink:#1d1d1f;
    --paper:#ffffff;
    --stage:#ffffff;
  }
  *{box-sizing:border-box;margin:0;padding:0}
  html,body{width:1200px;height:1200px;overflow:hidden;background:var(--stage)}
  body{position:relative;font-family:"Raleway",sans-serif;color:var(--ink)}

  .page{position:absolute;width:380px;height:537px;background:var(--paper);
    box-shadow:6px 8px 12px rgba(0,0,0,.22);overflow:hidden}
  .page--p4{left:59px;top:55px}
  .page--p5{left:747px;top:66px}
  .page--p6{left:58px;top:623px}
  .page--contact{left:747px;top:636px}

  /* header rule with page number */
  .page-head{position:absolute;left:0;top:0;width:100%;height:22px}
  .page-head .band{position:absolute;top:0;height:12px;background:var(--blue)}
  .page-head .rule{position:absolute;top:16px;height:3px;background:var(--blue)}
  .page-head .band.l,.page-head .rule.l{left:0;width:318px}
  .page-head .band.r,.page-head .rule.r{left:342px;right:0}
  .page-head .num{position:absolute;left:318px;width:24px;top:-2px;text-align:center;
    font:700 21px/24px "Poppins",sans-serif;color:var(--blue)}

  .title{position:absolute;left:39px;font:800 37px/38px "Raleway",sans-serif;
    color:var(--blue);letter-spacing:.3px;text-transform:uppercase}
  .title-bar{position:absolute;left:39px;width:103px;height:5px;background:var(--blue)}

  .block{position:absolute;left:39px;width:305px}
  .item-head{display:flex;align-items:flex-end;gap:6px;color:var(--blue)}
  .item-head .n{font:700 30px/28px "Poppins",sans-serif}
  .item-head .n i{font-style:normal;font-size:18px}
  .item-head .h{font:600 16px/18px "Poppins",sans-serif;padding-bottom:1px}
  .body{font:500 12px/15px "Raleway",sans-serif;color:var(--ink)}
  .item-head + .body{margin-top:8px}

  .photo{position:absolute;left:0;width:100%}
  .photo--team{top:363px;height:174px;
    background:linear-gradient(100deg,#6a4f36 0%,#c99255 30%,#e8e4de 50%,#b38a54 72%,#5a4a3a 100%)}

  .foot-deco{position:absolute;bottom:0;left:0;width:100%;height:22px}
  .foot-deco .bar{position:absolute;left:30px;bottom:0;width:61px;height:22px;background:var(--orange)}
  .foot-deco .sq{position:absolute;bottom:0;width:25px;height:22px;border:6px solid var(--orange);border-bottom-width:5px}
  .foot-deco .sq.a{left:233px}
  .foot-deco .sq.b{left:272px}

  /* contact page */
  .deco-square{position:absolute;left:14px;top:14px;width:44px;height:44px;background:var(--blue)}
  .deco-frame{position:absolute;right:0;top:0;width:71px;height:71px;border:13px solid var(--orange)}
  .brand{position:absolute;left:0;width:100%;top:40px;display:flex;justify-content:center;align-items:center;gap:9px}
  .brand .mark{width:26px;height:26px;border-radius:50%;background:var(--orange)}
  .brand .name{font:700 27px/30px "Raleway",sans-serif;color:var(--blue)}
  .cta{position:absolute;left:65px;top:100px;width:249px;height:41px;background:var(--orange);
    color:#fff;font:700 30px/41px "Poppins",sans-serif;text-align:center}
  .lead{position:absolute;left:0;width:100%;top:145px;text-align:center;
    font:700 16px/17px "Poppins",sans-serif;color:var(--blue)}
  .lead-body{position:absolute;left:0;width:100%;top:190px;text-align:center;font:500 12.5px/15px "Raleway",sans-serif}
  .photo--cleaning{top:239px;left:42px;width:296px;height:184px;
    background:linear-gradient(115deg,#4e4236 0%,#b8a58a 35%,#e5ddd0 60%,#cbb89a 100%)}
  .powered{position:absolute;left:42px;top:348px;width:296px;height:75px;background:rgba(230,154,0,.9);color:#fff}
  .powered .label{position:absolute;left:30px;top:6px;font:500 24px/29px "Raleway",sans-serif}
  .powered .divider{position:absolute;left:154px;top:8px;width:1px;height:56px;background:#fff}
  .powered .partner{position:absolute;left:166px;top:4px;width:120px;text-align:center}
  .powered .partner b{display:block;font:700 42px/46px "Poppins",sans-serif}
  .powered .partner small{display:block;font:500 9px/11px "Raleway",sans-serif}
  .info-title{position:absolute;left:0;width:100%;top:437px;text-align:center;font:600 16px/18px "Poppins",sans-serif;color:var(--blue)}
  .info-row{position:absolute;display:flex;align-items:center;gap:5px;font:600 12px/14px "Raleway",sans-serif}
  .info-row svg{width:20px;height:20px;flex:none}
  .info-row.phone{left:67px;top:465px}
  .info-row.web{left:204px;top:465px}
  .info-row.mail{left:136px;top:490px}
</style>
</head>
<body>

<!-- Page 4 -->
<section class="page page--p4">
  <div class="page-head"><span class="band l"></span><span class="rule l"></span><span class="num">4</span><span class="band r"></span><span class="rule r"></span></div>
  <h1 class="title" style="top:51px">Quality &amp;<br>Consistent<br>Services</h1>
  <div class="title-bar" style="top:165px"></div>
  <div class="block" style="top:180px">
    <div class="item-head"><span class="n">1<i>●</i></span><span class="h">Background Checks</span></div>
    <p class="body">We conduct comprehensive background checks on our service providers, guaranteeing your safety and peace of mind.</p>
  </div>
  <div class="block" style="top:271px">
    <div class="item-head"><span class="n">2<i>●</i></span><span class="h">Standards</span></div>
    <p class="body" style="margin-top:4px">Our providers adhere to strict service standards, ensuring the job is done right, every time. You're in capable hands with Quillora.</p>
  </div>
  <div class="photo photo--team" role="img" aria-label="Photo of a smiling cleaning team in blue aprons in a bright office"></div>
</section>

<!-- Page 5 -->
<section class="page page--p5">
  <div class="page-head"><span class="band l"></span><span class="rule l"></span><span class="num">5</span><span class="band r"></span><span class="rule r"></span></div>
  <h1 class="title" style="top:56px">Cost-<br>Effective<br>Solutions</h1>
  <div class="title-bar" style="top:168px"></div>
  <p class="block body" style="top:184px;width:325px">Our unique advantage lies in efficiency. By lining up jobs in the same building, we create economies of scale, which translates to lower costs for you.</p>
  <div class="block" style="top:237px;width:325px">
    <div class="item-head"><span class="n">1<i>●</i></span><span class="h">Economies of Scale</span></div>
    <p class="body" style="margin-top:9px">By centralizing multiple services in one location, Quillora creates economies of scale. This results in cost savings that are passed on to you, ensuring the best value for your home services.</p>
  </div>
  <div class="block" style="top:345px;width:325px">
    <div class="item-head"><span class="n">2<i>●</i></span><span class="h">Efficient Job Scheduling</span></div>
    <p class="body" style="margin-top:11px">Unlike traditional service providers who travel between jobs, Quillora lines up all jobs in the same building. This efficient scheduling eliminates the need for service providers to travel, reducing costs and ultimately lowering prices for you.</p>
  </div>
  <div class="foot-deco"><span class="bar"></span><span class="sq a"></span><span class="sq b"></span></div>
</section>

<!-- Page 6 -->
<section class="page page--p6">
  <div class="page-head"><span class="band l"></span><span class="rule l"></span><span class="num">6</span><span class="band r"></span><span class="rule r"></span></div>
  <h1 class="title" style="top:51px">Perfect<br>Balance of<br>Security &amp;<br>Convenience</h1>
  <div class="title-bar" style="top:204px"></div>
  <p class="block body" style="top:226px;width:300px">Quillora offers the perfect blend of security and convenience, ensuring your peace of mind and a hassle-free experience. With three varied access authority options", you're in ultimate control.</p>
  <div class="block" style="top:294px;width:320px">
    <div class="item-head" style="align-items:center"><span class="n">1<i>●</i></span><span class="h">Access Granted (via Temporary<br>Passcode):</span></div>
    <p class="body" style="margin-top:7px">For secure service provider access when you're away.</p>
  </div>
  <div class="block" style="top:362px;width:320px">
    <div class="item-head"><span class="n">2<i>●</i></span><span class="h">Knocking Only:</span></div>
    <p class="body" style="margin-top:2px">Choose this when you're home and want to unlock the door in person.</p>
  </div>
  <div class="block" style="top:434px;width:320px">
    <div class="item-head"><span class="n">3<i>●</i></span><span class="h">Do Not Disturb:</span></div>
    <p class="body" style="margin-top:2px">Opt for this if you prefer no access during the service, ensuring privacy and comfort.</p>
  </div>
  <div class="foot-deco"><span class="bar" style="left:39px"></span><span class="sq a" style="left:241px"></span><span class="sq b" style="left:280px"></span></div>
</section>

<!-- Back cover -->
<section class="page page--contact">
  <span class="deco-square"></span>
  <span class="deco-frame"></span>
  <div class="brand"><span class="mark"></span><span class="name">Quillora</span></div>
  <div class="cta">Contact Quillora</div>
  <p class="lead">Ready to experience the<br>convenience of Quillora?</p>
  <p class="lead-body">Reach out to our team today for inquiries,<br>bookings, or assistance.</p>
  <div class="photo photo--cleaning" role="img" aria-label="Photo of a cleaning team wiping tables in a bright dining room"></div>
  <div class="powered">
    <span class="label">Powered<br>by</span>
    <span class="divider"></span>
    <span class="partner"><b>OFR</b><small>Orfield Smart Home</small></span>
  </div>
  <p class="info-title">Contact Information</p>
  <div class="info-row phone">
    <svg viewBox="0 0 20 20"><circle cx="10" cy="10" r="9" fill="none" stroke="#e69a00" stroke-width="1.3"/><path d="M7 5.5l1.6 2.4-1 1.1c.6 1.3 1.5 2.2 2.8 2.8l1.1-1 2.4 1.6-.8 1.7c-3.6-.2-6.7-3.3-6.9-6.9z" fill="#e69a00"/></svg>
    <span>1300 555 014</span>
  </div>
  <div class="info-row web">
    <svg viewBox="0 0 20 20" fill="none" stroke="#e69a00" stroke-width="1.2"><circle cx="10" cy="10" r="9"/><circle cx="10" cy="10" r="5.5"/><ellipse cx="10" cy="10" rx="2.3" ry="5.5"/><path d="M4.5 10h11"/></svg>
    <span>www.quillora.au</span>
  </div>
  <div class="info-row mail">
    <svg viewBox="0 0 20 20"><circle cx="10" cy="10" r="9" fill="none" stroke="#e69a00" stroke-width="1.3"/><rect x="5" y="6.5" width="10" height="7" fill="#e69a00"/><path d="M5 6.5l5 4 5-4" fill="none" stroke="#fff" stroke-width="1"/></svg>
    <span>info@quillora.au</span>
  </div>
  <div class="foot-deco"><span class="bar"></span><span class="sq a"></span><span class="sq b"></span></div>
</section>

</body>
</html>
```